TVQ-Business Card Design

I need a modern, professional business card design that includes my logo as the main feature, maybe the entire background with the contact info overlaying or even contact info on the back and the logo full frontal

Neat and organized placement of contact information

Would like to see options in black and white

Target Market(s)

real estate Developers, Construction managers, business and home owners

Industry/Entity Type

Construction

Contact Information for Business Card

TVQ Construction
Dennis Fairweather
General Contractor

Office: 1-888-902-7351 Ext #1
Cell: 412-730-2168
Fax: 1-888-902-7351

Font styles to use
Serif

Requirements
Must have
• title
• office #
• cell #
• Email
• website
Nice to have
• fax

```html
<!DOCTYPE html>
<html lang="en">
<head>
<meta charset="utf-8">
<title>TVQ Construction – Business Card</title>
<link rel="stylesheet" href="https://fonts.googleapis.com/css2?family=Nunito:wght@600;700;800&display=swap">
<style>
  :root {
    --page-bg: #e9e7e3;
    --card-white: #ffffff;
    --card-black: #060808;
    --green-dark: #1d7a3b;
    --green-mid: #3f9f43;
    --green-light: #8cc63f;
    --ink: #2b2b2b;
    --white: #ffffff;
  }
  * { box-sizing: border-box; margin: 0; padding: 0; }
  html, body {
    width: 1200px; height: 1200px; overflow: hidden;
    background: var(--page-bg);
    font-family: "Nunito", sans-serif;
  }
  .canvas { position: relative; width: 1200px; height: 1200px; }

  .card {
    position: absolute; left: 160px;
    width: 880px; height: 503px;
    border-radius: 36px; overflow: hidden;
    box-shadow: 0 14px 30px rgba(0,0,0,0.18);
  }
  .card-front { top: 60px; background: var(--card-white); }
  .card-back  { top: 627px; background: var(--card-black);
    display: flex; align-items: center; justify-content: center; }

  .front-band { position: absolute; inset: 0; width: 100%; height: 100%; }

  .brand {
    position: absolute; left: 64px; top: 150px;
    display: flex; align-items: center; gap: 14px;
    max-width: 380px; white-space: nowrap;
  }
  .brand-mark { width: 26px; height: 26px; background: var(--green-mid); flex: none; }
  .brand-name {
    font-weight: 800; font-size: 34px; color: var(--green-mid);
    letter-spacing: 0.3px;
  }

  .person { position: absolute; left: 64px; top: 386px; color: var(--white); }
  .person-name { font-weight: 800; font-size: 36px; line-height: 1.1; }
  .person-title { font-weight: 700; font-size: 24px; margin-top: 4px; }

  .contacts {
    position: absolute; left: 470px; top: 52px;
    list-style: none; color: var(--ink);
    font-weight: 600; font-size: 22px; white-space: nowrap;
  }
  .contacts li { display: flex; align-items: center; gap: 12px; height: 36px; }
  .contacts li.gap { margin-top: 18px; }
  .contact-icon { width: 22px; height: 22px; flex: none; }

  .website {
    position: absolute; left: 540px; top: 302px;
    color: var(--white); font-weight: 700; font-size: 24px; letter-spacing: 0.4px;
    white-space: nowrap;
  }

  .back-name {
    font-weight: 800; font-size: 78px; color: var(--green-mid); letter-spacing: 1px;
  }
</style>
</head>
<body>
<main class="canvas">

  <section class="card card-front" aria-label="Business card front">
    <svg class="front-band" viewBox="0 0 880 503" preserveAspectRatio="none" aria-hidden="true">
      <defs>
        <linearGradient id="bandGrad" x1="0" y1="1" x2="1" y2="0">
          <stop offset="0" stop-color="#5aae46"/>
          <stop offset="0.5" stop-color="#2f8a3e"/>
          <stop offset="1" stop-color="#1d7a3b"/>
        </linearGradient>
      </defs>
      <polygon points="0,342 462,342 512,232 880,232 880,252 522,252 474,362 0,362" fill="var(--green-light)"/>
      <polygon points="0,362 474,362 522,252 880,252 880,503 0,503" fill="url(#bandGrad)"/>
      <polygon points="0,470 880,470 880,486 0,486" fill="var(--green-light)"/>
    </svg>

    <div class="brand">
      <span class="brand-mark"></span>
      <span class="brand-name">TVQ Construction</span>
    </div>

    <ul class="contacts">
      <li>
        <svg class="contact-icon" viewBox="0 0 22 22" aria-hidden="true"><circle cx="11" cy="11" r="11" fill="var(--green-mid)"/><rect x="6" y="8" width="10" height="7" rx="1" fill="#fff"/><rect x="8" y="5" width="6" height="3" fill="#fff"/></svg>
        1-888-902-7351
      </li>
      <li>
        <svg class="contact-icon" viewBox="0 0 22 22" aria-hidden="true"><circle cx="11" cy="11" r="11" fill="var(--green-mid)"/><path d="M6 9c0-2 2-3 5-3s5 1 5 3l-2 1-1-2h-4l-1 2zM7 11h8v4H7z" fill="#fff"/></svg>
        1-888-902-7351 Ext #1
      </li>
      <li class="gap">
        <svg class="contact-icon" viewBox="0 0 22 22" aria-hidden="true"><circle cx="11" cy="11" r="11" fill="var(--green-mid)"/><rect x="8" y="5" width="6" height="12" rx="1.5" fill="#fff"/></svg>
        412-730-2168
      </li>
      <li>
        <svg class="contact-icon" viewBox="0 0 22 22" aria-hidden="true"><circle cx="11" cy="11" r="11" fill="var(--green-mid)"/><rect x="5" y="7" width="12" height="8" rx="1.5" fill="#fff"/><path d="M5.5 7.5 11 12l5.5-4.5" stroke="var(--green-mid)" stroke-width="1.2" fill="none"/></svg>
        dennis@tvqconstruction.com
      </li>
    </ul>

    <div class="person">
      <p class="person-name">Dennis Fairweather</p>
      <p class="person-title">General Contractor</p>
    </div>

    <p class="website">www.tvqconstruction.com</p>
  </section>

  <section class="card card-back" aria-label="Business card back">
    <p class="back-name">TVQ Construction</p>
  </section>

</main>
</body>
</html>
```